Orvel Prime - Letter Head

My company is a residential and commercial cleaning company , which is located in Abu Dhabi, UAE.
I am looking for a creative letterhead reflects the professional and reflects professionalism and send the feeling of relax and comfort.
The color which will be used it has to be selected carefully in prospective of colors psychological effects, so every color to be used should be for a reason.
Also, reflecting my company colors in an attractive way.
Regarding the information which it should contains, it has to show the address, contacts , telephones an, email address and website.
Also, my company logo is attached
Residential

```html
<!DOCTYPE html>
<html lang="en">
<head>
<meta charset="utf-8">
<title>Orvel Prime – Letterhead</title>
<link rel="stylesheet" href="https://fonts.googleapis.com/css2?family=Nunito:wght@600;800&display=swap">
<style>
  :root {
    --brand-blue: #0a57a6;
    --brand-green: #a4cb3a;
    --watermark-tint: #eef4e4;
    --watermark-ring: #f1f6e6;
    --paper: #ffffff;
    --on-blue: #ffffff;
  }
  html, body {
    margin: 0;
    padding: 0;
    width: 1200px;
    height: 1000px;
    overflow: hidden;
    background: var(--paper);
  }
  .canvas {
    position: relative;
    width: 1200px;
    height: 1000px;
    background: var(--paper);
  }
  .letterhead {
    position: absolute;
    left: 304px;
    top: 0;
    width: 618px;
    height: 932px;
    background: var(--paper);
    overflow: hidden;
  }
  .brand {
    position: absolute;
    left: 18px;
    top: 76px;
    display: flex;
    align-items: center;
    gap: 10px;
  }
  .brand-dot {
    width: 40px;
    height: 40px;
    border-radius: 50%;
    background: var(--brand-green);
  }
  .brand-name {
    font-family: "Nunito", sans-serif;
    font-weight: 800;
    font-size: 30px;
    line-height: 1;
    color: var(--brand-blue);
    letter-spacing: -0.5px;
  }
  .watermark {
    position: absolute;
    left: 170px;
    top: 316px;
    width: 310px;
    height: 310px;
    border-radius: 50%;
    border: 8px solid var(--watermark-ring);
    box-sizing: border-box;
    display: flex;
    align-items: center;
    justify-content: center;
  }
  .watermark-name {
    font-family: "Nunito", sans-serif;
    font-weight: 800;
    font-size: 40px;
    color: var(--watermark-tint);
    white-space: nowrap;
  }
  .footer-wave {
    position: absolute;
    left: 0;
    bottom: 0;
    width: 618px;
    height: 92px;
    display: block;
  }
  .contact {
    position: absolute;
    left: 24px;
    right: 24px;
    bottom: 10px;
    display: flex;
    flex-wrap: wrap;
    justify-content: center;
    gap: 4px 18px;
    margin: 0;
    padding: 0;
    list-style: none;
    font-family: "Nunito", sans-serif;
    font-weight: 600;
    font-size: 11px;
    line-height: 14px;
    color: var(--on-blue);
    white-space: nowrap;
  }
  .contact-item {
    display: flex;
    align-items: center;
    gap: 5px;
  }
  .contact-icon {
    width: 10px;
    height: 10px;
    flex: none;
  }
</style>
</head>
<body>
<div class="canvas">
  <div class="letterhead">
    <header class="brand">
      <span class="brand-dot"></span>
      <span class="brand-name">Orvel Prime</span>
    </header>

    <div class="watermark" aria-hidden="true">
      <span class="watermark-name">Orvel Prime</span>
    </div>

    <svg class="footer-wave" viewBox="0 0 618 92" preserveAspectRatio="none" aria-hidden="true">
      <path d="M0,30 C200,46 380,42 490,20 C580,2 612,20 618,28 L618,34 C610,25 580,8 490,26 C380,48 200,52 0,38 Z" fill="var(--brand-green)"/>
      <path d="M0,37 C200,51 380,47 490,25 C580,7 610,25 618,34 L618,92 L0,92 Z" fill="var(--brand-blue)"/>
    </svg>

    <ul class="contact">
      <li class="contact-item">
        <svg class="contact-icon" viewBox="0 0 10 10" aria-hidden="true"><path d="M5 0.5a3.2 3.2 0 0 0-3.2 3.2C1.8 6 5 9.5 5 9.5s3.2-3.5 3.2-5.8A3.2 3.2 0 0 0 5 0.5z" fill="var(--brand-green)"/><circle cx="5" cy="3.7" r="1.1" fill="var(--brand-blue)"/></svg>
        Unit 14, Lumen Court, Harbor District, Sample City
      </li>
      <li class="contact-item">
        <svg class="contact-icon" viewBox="0 0 10 10" aria-hidden="true"><path d="M2.2 0.8l1.6 1.9-0.9 1.1a6 6 0 0 0 3.3 3.3l1.1-0.9 1.9 1.6-0.8 1.4C4.6 9.2 0.8 5.4 0.8 1.6z" fill="var(--brand-green)"/></svg>
        +00 123 456 7890
      </li>
      <li class="contact-item">
        <svg class="contact-icon" viewBox="0 0 10 10" aria-hidden="true"><rect x="0.5" y="2" width="9" height="6.5" rx="1" fill="var(--brand-green)"/><path d="M0.8 2.5L5 5.8l4.2-3.3" fill="none" stroke="var(--brand-blue)" stroke-width="0.9"/></svg>
        hello@orvelprime.example
      </li>
      <li class="contact-item">
        <svg class="contact-icon" viewBox="0 0 10 10" aria-hidden="true"><circle cx="5" cy="5" r="4.3" fill="none" stroke="var(--brand-green)" stroke-width="1"/><path d="M0.7 5h8.6M5 0.7c-2.2 2.4-2.2 6.2 0 8.6M5 0.7c2.2 2.4 2.2 6.2 0 8.6" fill="none" stroke="var(--brand-green)" stroke-width="0.8"/></svg>
        www.orvelprime.example
      </li>
    </ul>
  </div>
</div>
</body>
</html>
```